Packaging label for launch of sun dried tomato products.

Established family farm in South Africa growing fruit for the production of dried fruit. We need a packaging label for the launch of our sun dried tomato products ie dried tomatoes in olive oil, dried tomato flakes and tomato powder. Packaging will be a round glass "jam jar" and spice shaker bottle. Due to limited amount of product available we cannot market to the masses, but rather focus on conveying a message of quality and exclusivity.

Target Market(s)

Home chef

Industry/Entity Type

Food

Font styles to use
Serif

Requirements
Nice to have
• Include the farm name in the design. KEVANTO

```html
<!DOCTYPE html>
<html lang="en">
<head>
<meta charset="UTF-8">
<title>Kevanto Sun Dried Tomato Labels</title>
<link href="https://fonts.googleapis.com/css2?family=Montserrat:wght@700;800&family=Rye&family=Kaushan+Script&display=swap" rel="stylesheet">
<style>
  :root {
    --canvas: #ffffff;
    --label-light: #f5f5f5;
    --label-mid: #e4e4e4;
    --ink: #111111;
    --tomato-red: #d71920;
    --tomato-deep: #b8141a;
    --powder-rust: #c4451d;
    --leaf-green: #4f7d1e;
    --wood-grey: #7b7b7b;
    --brand-black: #141414;
    --brand-red: #d71920;
    --brand-green: #4f7d1e;
    --band: #1a1a1a;
    --band-text: #ffffff;
  }
  * { box-sizing: border-box; margin: 0; padding: 0; }
  html, body {
    width: 1200px; height: 738px; overflow: hidden;
    background: var(--canvas);
  }
  .label-range {
    width: 1200px; height: 738px;
    display: flex; justify-content: center; align-items: center; gap: 30px;
  }
  .label {
    position: relative;
    width: 360px; height: 335px;
    overflow: hidden;
    background: linear-gradient(170deg, var(--label-light) 0%, #ffffff 45%, var(--label-mid) 100%);
    box-shadow: 0 6px 12px rgba(0,0,0,0.12);
  }
  .label--flakes {
    background: linear-gradient(180deg, #f3f3f3 0%, #e8e8e8 28%, #b4b4b4 52%, #8a8a8a 100%);
  }

  .brand {
    position: absolute; top: 14px; left: 0; right: 0;
    display: flex; justify-content: center; align-items: center; gap: 7px;
    font-family: 'Montserrat', sans-serif; font-weight: 800;
    font-size: 17px; letter-spacing: 1px; color: var(--ink);
    z-index: 3;
  }
  .brand-square { width: 14px; height: 14px; }
  .label--powder .brand-square { background: var(--brand-black); }
  .label--flakes .brand-square { background: var(--brand-red); }
  .label--oil .brand-square { background: var(--brand-green); }

  .title-kicker {
    position: absolute; top: 74px; left: 0; right: 0; text-align: center;
    font-family: 'Montserrat', sans-serif; font-weight: 800;
    font-size: 25px; line-height: 1; letter-spacing: 5px; color: var(--ink); z-index: 3;
  }
  .title-main {
    position: absolute; top: 98px; left: 0; right: 0; text-align: center;
    font-family: 'Rye', serif; font-weight: 400; font-size: 64px; line-height: 1;
    color: var(--tomato-red); letter-spacing: 0; z-index: 3;
  }
  .title-variant {
    position: absolute; top: 164px; left: 0; right: 0; text-align: center;
    font-family: 'Kaushan Script', cursive; font-size: 24px; line-height: 1.2;
    color: var(--leaf-green); z-index: 3;
  }
  .label--flakes .title-variant { color: #ffffff; }

  .photo { position: absolute; left: 0; right: 0; bottom: 0; }
  .photo--powder {
    top: 200px;
    background:
      linear-gradient(180deg, rgba(255,255,255,1) 0%, rgba(255,255,255,0) 30%),
      linear-gradient(90deg, var(--tomato-red) 0%, var(--powder-rust) 35%, var(--powder-rust) 65%, var(--tomato-red) 100%);
  }
  .photo--flakes {
    top: 190px;
    background:
      linear-gradient(180deg, rgba(180,180,180,1) 0%, rgba(180,180,180,0) 35%),
      linear-gradient(90deg, var(--wood-grey) 0%, #8a3a30 30%, #a3232a 55%, var(--tomato-red) 80%, #c42a22 100%);
  }
  .photo--oil {
    top: 200px;
    background:
      linear-gradient(180deg, rgba(255,255,255,1) 0%, rgba(255,255,255,0) 40%),
      linear-gradient(90deg, var(--tomato-deep) 0%, var(--tomato-red) 50%, var(--tomato-deep) 100%);
  }
  .photo-corner {
    position: absolute; top: -30px; width: 110px; height: 110px;
    border-radius: 50%;
    background: radial-gradient(circle at 50% 55%, #e2372a 0%, var(--tomato-red) 55%, var(--tomato-deep) 100%);
  }
  .photo-corner--left { left: -40px; }
  .photo-corner--right { right: -40px; }

  .farm-band {
    position: absolute; left: 35px; right: 35px; bottom: 18px; height: 20px;
    background: var(--band); color: var(--band-text);
    font-family: 'Montserrat', sans-serif; font-weight: 700;
    font-size: 10.5px; letter-spacing: 0.2px;
    display: flex; align-items: center; justify-content: center;
    z-index: 3;
  }
</style>
</head>
<body>
<main class="label-range">

  <section class="label label--powder">
    <div class="photo-corner photo-corner--left" role="img" aria-label="Fresh whole tomato"></div>
    <div class="photo-corner photo-corner--right" role="img" aria-label="Fresh tomatoes and a tomato half"></div>
    <div class="brand"><span class="brand-square"></span><span>KEVANTO</span></div>
    <p class="title-kicker">SUN DRIED</p>
    <h1 class="title-main">TOMATO</h1>
    <div class="photo photo--powder" role="img" aria-label="Heap of red tomato powder among fresh tomatoes"></div>
    <p class="title-variant">in tomato powder</p>
    <p class="farm-band">ESTABLISHED FAMILY FARM IN SOUTH AFRICA</p>
  </section>

  <section class="label label--flakes">
    <div class="brand"><span class="brand-square"></span><span>KEVANTO</span></div>
    <p class="title-kicker">SUN DRIED</p>
    <h1 class="title-main">TOMATO</h1>
    <div class="photo photo--flakes" role="img" aria-label="Bowl of dried tomato flakes with herbs and cherry tomatoes on a wooden table"></div>
    <p class="title-variant">in dried tomato flakes</p>
    <p class="farm-band">ESTABLISHED FAMILY FARM IN SOUTH AFRICA</p>
  </section>

  <section class="label label--oil">
    <div class="brand"><span class="brand-square"></span><span>KEVANTO</span></div>
    <p class="title-kicker">SUN DRIED</p>
    <h1 class="title-main">TOMATO</h1>
    <div class="photo photo--oil" role="img" aria-label="Watercolour tomatoes with green splashes"></div>
    <p class="title-variant">in olive oil</p>
    <p class="farm-band">ESTABLISHED FAMILY FARM IN SOUTH AFRICA</p>
  </section>

</main>
</body>
</html>
```